Zertifikat-Design für Bildungsträger im Bereich der Erwachsenenbildung
Zielgruppe
Talwerk Akademie - Zertifizierter Bildungsträger im Bereich der Erwachsenenbildung. Überwiegend Mitarbeiter in Unternehmen.
Aufgabenstellung
'Erstelle ein hochwertiges, modernes und exklusiv wirkendes Zertifikat für die Talwerk Akademie. Das Design soll professionell, minimalistisch und zugleich edel sein. Ziel ist es, ein Dokument zu gestalten, das den Eindruck vermittelt: 'Das ist das einzige und beste Zertifikat in der ganzen verdammten Welt.'
Das Zertifikat soll im Querformat (idealerweise DIN A4 horizontal) gestaltet werden. Der Inhalt soll zweisprachig (Deutsch und Englisch) dargestellt werden, klar gegliedert und typografisch hochwertig aufgebaut. Alle Inhalte sollten mittig ausgerichtet sein, mit gut erkennbarer visueller Hierarchie.
Der Haupttext lautet wie folgt:
'Talwerk Akademie gratuliert 'Name / Platzhalter' zum erfolgreichen Abschluss des Kurses 'Platzhalter' Datum, Unterschrift (siehe unten)
+englisch
'Talwerk Akademie hereby certifies that [Name of Participant / Placeholder] has successfully participated on 'date'.
Darunter sollen zwei stilisierte Unterschriften platziert werden – gerne von Hand gezeichnet oder elegant typografisch umgesetzt. Die Beschriftung unter den Unterschriften lautet: 'Leitung Talwerk Akademie'.
Ein zentrales Element ist das Hologramm. Muster das gelieferte Bild 'Hologramm.png'. Es muss deutlich sichtbar und hochwertig integriert werden. Die Aufschrift 'Talwerk' im Hologramm muss klar erkennbar sein. Idealer Platz wäre unten links oder rechts, eventuell mit einer leichten 3D-Anmutung oder Glanzeffekt.
Das gesamte Design muss der Corporate Identity der Talwerk Akademie entsprechen. Die verwendeten Farben sind: Hauptfarbe Dunkelblau (RGB 14, 32, 62), ergänzt durch Hellblau (RGB 241, 245, 250), ein zusätzliches Blau (RGB 65, 111, 174), Pink (RGB 140, 130, 227), Dunkellila (RGB 169, 97, 161), sowie Gelb (RGB 248, 216, 73) und Orange (RGB 220, 121, 70) für gezielte Akzente.
Als Schriftart ist ausschließlich Roboto zu verwenden. Der Name des Teilnehmers soll besonders hervorgehoben werden (z...

```html
<!DOCTYPE html>
<html lang="de">
<head>
<meta charset="utf-8">
<title>Talwerk Akademie – Zertifikat</title>
<link rel="stylesheet" href="https://fonts.googleapis.com/css2?family=Roboto:wght@400;500;700&display=swap">
<style>
  :root {
    --navy: #0e203e;
    --stage: #1e3a5e;
    --paper: #f3efe6;
    --ice: #f1f5fa;
    --blue: #416fae;
    --pink: #8c82e3;
    --plum: #a961a1;
    --yellow: #f8d849;
    --orange: #dc7946;
  }
  * { margin: 0; padding: 0; box-sizing: border-box; }
  html, body {
    width: 1200px;
    height: 1200px;
    overflow: hidden;
    background: var(--stage);
    font-family: "Roboto", sans-serif;
    color: var(--navy);
  }
  .certificate {
    position: absolute;
    left: 0;
    top: 111px;
    width: 1200px;
    height: 978px;
    background: var(--paper);
  }
  .certificate__frame {
    position: absolute;
    inset: 41px 26px;
    border: 2px solid var(--navy);
  }
  .centered {
    position: absolute;
    left: 0;
    width: 100%;
    text-align: center;
    transform: translateY(-50%);
    white-space: nowrap;
  }
  .brand {
    position: absolute;
    left: 424px;
    top: 105px;
    display: flex;
    align-items: center;
    gap: 30px;
  }
  .brand__square {
    width: 80px;
    height: 80px;
    background: var(--navy);
    border-radius: 6px;
  }
  .brand__name {
    font-weight: 700;
    font-size: 37px;
    line-height: 1.08;
    letter-spacing: 0.06em;
    text-transform: uppercase;
    color: var(--navy);
  }
  .title {
    top: 279px;
    font-size: 94px;
    font-weight: 700;
    letter-spacing: 0.07em;
  }
  .subtitle {
    top: 361px;
    font-size: 54px;
    font-weight: 700;
    letter-spacing: 0.08em;
  }
  .body-text {
    font-size: 30px;
    font-weight: 400;
  }
  .congrats { top: 445px; }
  .participant {
    top: 519px;
    font-size: 84px;
    font-weight: 700;
    letter-spacing: 0.02em;
  }
  .course { top: 586px; }
  .certifies { top: 655px; }
  .participated { top: 707px; }
  .signature {
    position: absolute;
    top: 760px;
    height: 145px;
  }
  .signature--left { left: 141px; width: 320px; }
  .signature--right { left: 580px; width: 290px; }
  .signature__mark {
    height: 80px;
    margin: 0 20px;
    background: linear-gradient(180deg, rgba(14,32,62,0) 0%, rgba(14,32,62,0.08) 100%);
    border-radius: 4px;
  }
  .signature__line {
    height: 1.5px;
    background: var(--navy);
    margin-top: 8px;
  }
  .signature__label {
    margin-top: 22px;
    text-align: center;
    font-size: 20px;
    font-weight: 400;
  }
  .seal {
    position: absolute;
    left: 918px;
    top: 708px;
    width: 194px;
    height: 194px;
  }
</style>
</head>
<body>
  <main class="certificate">
    <div class="certificate__frame"></div>

    <div class="brand">
      <div class="brand__square"></div>
      <div class="brand__name">Talwerk<br>Akademie</div>
    </div>

    <h1 class="centered title">ZERTIFIKAT</h1>
    <h2 class="centered subtitle">CERTIFICATE</h2>

    <p class="centered body-text congrats">Talwerk Akademie gratuliert</p>
    <p class="centered participant">NAME</p>
    <p class="centered body-text course">zum erfolgreichen Abschluss des Kurses</p>
    <p class="centered body-text certifies">Talwerk Akademie hereby certifies-that</p>
    <p class="centered body-text participated">has successfully participated on</p>

    <div class="signature signature--left">
      <div class="signature__mark" role="img" aria-label="Handschriftliche Unterschrift der Akademieleitung"></div>
      <div class="signature__line"></div>
      <p class="signature__label">Leitung Talwerk Akademie</p>
    </div>

    <div class="signature signature--right">
      <div class="signature__mark" role="img" aria-label="Handschriftliche Unterschrift der Akademieleitung"></div>
      <div class="signature__line"></div>
      <p class="signature__label">Leitung Talwerk Akademie</p>
    </div>

    <svg class="seal" viewBox="0 0 194 194" role="img" aria-label="Hologramm-Siegel der Akademie">
      <defs>
        <linearGradient id="seal-rim" x1="0" y1="0" x2="1" y2="1">
          <stop offset="0" stop-color="#f8d849"/>
          <stop offset="0.5" stop-color="#c9a64a"/>
          <stop offset="1" stop-color="#f8d849"/>
        </linearGradient>
        <radialGradient id="seal-foil" cx="0.45" cy="0.4" r="0.7">
          <stop offset="0" stop-color="#8fd3f0"/>
          <stop offset="0.4" stop-color="#8c82e3"/>
          <stop offset="0.75" stop-color="#416fae"/>
          <stop offset="1" stop-color="#a961a1"/>
        </radialGradient>
      </defs>
      <circle cx="97" cy="97" r="95" fill="url(#seal-rim)"/>
      <circle cx="97" cy="97" r="88" fill="url(#seal-foil)"/>
    </svg>
  </main>
</body>
</html>
```